Builders Worksite Corflute Outdoor Sign

We are a building company who are just branching out into new construction. How first new build is our own home which was designed by us and a local architect. We are proud and want to create more advertisement around our business.

We need a corflute sign that can staked outside the construction site and can be seen by people passing by.
Updates

Can we please make the company name and logo bigger (Tidewater Ridge Homes) This needs to be the focus. Can we please replace 'Manu' with 'Contact Us on 021-574-3619'

Target Market(s)

Home owners and people wishing to build on lifestyle blocks in New Zealand.

Font styles to use
Sans Serif

Requirements
Must have
• It needs to feature our:
Logo
Company name
Contact name and number - Manu - 0215743619
Landscape NOT portrait.

```html
<!DOCTYPE html>
<html lang="en">
<head>
<meta charset="UTF-8">
<title>Tidewater Ridge Homes – Site Sign</title>
<link rel="stylesheet" href="https://fonts.googleapis.com/css2?family=Jost:wght@400&family=Montserrat:wght@900&display=swap">
<style>
  :root {
    --navy: #1a2030;
    --yellow: #f7c614;
    --yellow-light: #fbe07a;
    --gold: #d9a52a;
    --white: #ffffff;
    --silver: #e6e7e9;
    --page: #eeeeec;
  }
  * { box-sizing: border-box; margin: 0; padding: 0; }
  html, body {
    width: 779px;
    height: 1200px;
    overflow: hidden;
    background: var(--page);
  }
  .canvas {
    position: relative;
    width: 779px;
    height: 1200px;
  }
  .sign {
    position: absolute;
    left: 40px;
    top: 337px;
    width: 700px;
    height: 525px;
    display: grid;
    grid-template-rows: 201px 194px 130px;
    box-shadow: 0 8px 22px rgba(0,0,0,0.18);
    overflow: hidden;
  }
  .brand-band {
    display: grid;
    grid-template-columns: 150px 1fr;
    background: linear-gradient(90deg, var(--silver), var(--white));
  }
  .brand-block {
    background: var(--yellow);
    display: flex;
    align-items: center;
    justify-content: center;
  }
  .brand-dot {
    width: 96px;
    height: 96px;
    border-radius: 50%;
    background: var(--navy);
  }
  .brand-name {
    display: flex;
    flex-direction: column;
    align-items: center;
    justify-content: center;
    font-family: "Jost", sans-serif;
    font-weight: 400;
    color: var(--navy);
    text-transform: uppercase;
    line-height: 1;
    white-space: nowrap;
  }
  .brand-name .company { font-size: 52px; letter-spacing: 1px; }
  .brand-name .division { font-size: 34px; letter-spacing: 18px; margin-top: 20px; padding-left: 18px; }
  .contact-band {
    background: var(--navy);
    display: flex;
    align-items: center;
    justify-content: center;
  }
  .contact-line {
    font-family: "Montserrat", sans-serif;
    font-weight: 900;
    font-size: 70px;
    line-height: 1.1;
    letter-spacing: -1px;
    white-space: nowrap;
    background: linear-gradient(180deg, var(--yellow-light), var(--yellow));
    -webkit-background-clip: text;
    background-clip: text;
    color: transparent;
  }
  .phone-band {
    background: linear-gradient(180deg, var(--yellow-light), var(--yellow) 70%);
    display: flex;
    align-items: center;
    justify-content: center;
    gap: 14px;
  }
  .phone-icon { width: 52px; height: 52px; flex: none; }
  .phone-number {
    font-family: "Montserrat", sans-serif;
    font-weight: 900;
    font-size: 66px;
    line-height: 1;
    color: var(--navy);
    letter-spacing: -1px;
    white-space: nowrap;
  }
</style>
</head>
<body>
<main class="canvas">
  <section class="sign">
    <header class="brand-band">
      <div class="brand-block"><span class="brand-dot"></span></div>
      <div class="brand-name">
        <span class="company">Tidewater Ridge</span>
        <span class="division">Homes</span>
      </div>
    </header>
    <div class="contact-band">
      <span class="contact-line">Contact Us on</span>
    </div>
    <footer class="phone-band">
      <svg class="phone-icon" viewBox="0 0 54 54" aria-hidden="true">
        <path fill="#1a2030" d="M10 6c3-2 6-1 7 2l4 8c1 3 0 5-2 6l-3 2c2 6 7 11 13 14l2-3c1-2 4-3 6-2l8 4c3 1 4 4 2 7l-3 4c-2 2-5 3-8 2C23 45 9 31 5 17c-1-3 0-6 2-8z"/>
        <path fill="none" stroke="#1a2030" stroke-width="4" stroke-linecap="round" d="M30 14a10 10 0 0 1 10 10M31 5a19 19 0 0 1 18 18"/>
      </svg>
      <span class="phone-number">021-574-3619</span>
    </footer>
  </section>
</main>
</body>
</html>
```